Billboard design 8x3M LUMA (Spanish company)

We´re located in the south of Spain. We run a local telecom company.
We sell Fiber optic, and mobile phone lines mainly.
The billboard will have to be in Spanish, I would like the price to be something you spot on first sight when passing by in the car.
Our company color is blue, like in our logo which I will add. I will also add a example from what we currently have.
The new offer should be:
1000 megas + 100Gigas movil con llamadas ilimitadas. (meaning 1000Mb fiber optic speed and 100Gb data and unlimited calls for 1 mobile line)
Our details are: phone line 956 47 8092
Website: lu-ma.es

```html
<!DOCTYPE html>
<html lang="es">
<head>
<meta charset="utf-8">
<title>LUMA – Valla 8x3</title>
<link rel="stylesheet" href="https://fonts.googleapis.com/css2?family=Poppins:wght@500;600;700;800&display=swap">
<style>
  :root{
    --backdrop:#6f86a6;
    --brand-blue:#2a8dc1;
    --ring-blue:#2179aa;
    --deep-navy:#1b4257;
    --offer-yellow:#f7c300;
    --ink:#0d1b2a;
    --white:#ffffff;
    --badge-black:#080b10;
  }
  *{margin:0;padding:0;box-sizing:border-box}
  html,body{width:1200px;height:780px;overflow:hidden}
  body{background:var(--backdrop);font-family:"Poppins",sans-serif;position:relative}
  .billboard{position:absolute;left:40px;top:180px;width:1120px;height:420px;overflow:hidden;background:var(--brand-blue)}
  .billboard__bg,.billboard__visual{position:absolute;left:0;top:0}
  .price-badge{position:absolute;left:190px;top:235px;width:132px;height:132px;border-radius:50%;background:var(--badge-black);color:var(--white);display:flex;flex-direction:column;align-items:center;justify-content:center;line-height:1}
  .price-badge__label{font-size:20px;font-weight:600;margin-bottom:4px}
  .price-badge__amount{font-size:52px;font-weight:700;letter-spacing:-2px}
  .offer{position:absolute;left:330px;top:14px;width:380px;text-align:center;line-height:1}
  .offer__speed{font-size:124px;font-weight:800;color:var(--offer-yellow);letter-spacing:-4px}
  .offer__unit{display:inline-block;margin-top:2px;background:var(--brand-blue);color:var(--white);font-size:56px;font-weight:700;padding:6px 34px 8px;border-radius:10px;width:360px}
  .offer__data{font-size:88px;font-weight:800;color:var(--offer-yellow);letter-spacing:-3px;margin-top:4px;white-space:nowrap}
  .offer__detail{font-size:33px;font-weight:600;color:var(--white);line-height:1.15;margin-top:6px}
  .brand{position:absolute;left:770px;top:30px;width:330px;text-align:center;color:var(--white)}
  .brand__name{font-size:104px;font-weight:700;line-height:1;letter-spacing:4px}
  .brand__services{font-size:25px;font-weight:600;margin-top:6px;white-space:nowrap}
  .contact-arrow{position:absolute;left:718px;top:170px}
  .contact-phone-icon{position:absolute;left:905px;top:165px}
  .contact{position:absolute;left:750px;top:282px;width:370px;text-align:center;line-height:1.2;white-space:nowrap}
  .contact__phone{font-size:46px;font-weight:700;color:var(--white)}
  .contact__web{font-size:40px;font-weight:800;color:var(--ink)}
</style>
</head>
<body>
  <div class="billboard">
    <svg class="billboard__bg" width="1120" height="420" viewBox="0 0 1120 420">
      <path d="M0 0H700C800 100 800 320 700 420H0Z" fill="var(--ring-blue)"/>
      <path d="M0 0H670C765 100 765 320 670 420H0Z" fill="var(--deep-navy)"/>
      <path d="M335 0C255 100 255 320 335 420H0V0Z" fill="var(--offer-yellow)"/>
    </svg>
    <svg class="billboard__visual" width="340" height="420" viewBox="0 0 340 420" role="img" aria-label="Ilustración de un cohete luminoso despegando entre estrellas azules">
      <defs>
        <radialGradient id="spaceGlow" cx="45%" cy="50%" r="70%">
          <stop offset="0" stop-color="#1f7fc2"/>
          <stop offset="0.55" stop-color="#0b3a6a"/>
          <stop offset="1" stop-color="#041228"/>
        </radialGradient>
      </defs>
      <path d="M315 0C235 100 235 320 315 420H0V0Z" fill="url(#spaceGlow)"/>
    </svg>
    <div class="price-badge">
      <span class="price-badge__label">por</span>
      <span class="price-badge__amount">35€</span>
    </div>
    <div class="offer">
      <div class="offer__speed">1000</div>
      <div class="offer__unit">MEGAS</div>
      <div class="offer__data">+ 100Gb</div>
      <div class="offer__detail">movil con llamadas<br>ilimitadas</div>
    </div>
    <div class="brand">
      <div class="brand__name">LUMA</div>
      <div class="brand__services">Wifi | Fibra | Movil | Tv</div>
    </div>
    <svg class="contact-arrow" width="190" height="90" viewBox="0 0 190 90">
      <path d="M8 30C65 -5 140 5 168 60" fill="none" stroke="var(--ink)" stroke-width="5" stroke-linecap="round"/>
      <path d="M153 55L176 82L180 46Z" fill="var(--ink)"/>
    </svg>
    <svg class="contact-phone-icon" width="70" height="110" viewBox="0 0 70 110">
      <rect x="4" y="4" width="62" height="102" rx="10" fill="none" stroke="var(--white)" stroke-width="5"/>
      <line x1="26" y1="16" x2="44" y2="16" stroke="var(--white)" stroke-width="4" stroke-linecap="round"/>
      <circle cx="35" cy="90" r="5" fill="var(--white)"/>
    </svg>
    <div class="contact">
      <div class="contact__phone">956 47 8092</div>
      <div class="contact__web">www.lu-ma.es</div>
    </div>
  </div>
</body>
</html>
```